Restaurant Menus Designs (Lunch, Brunch, Dinner and Beverage/Dessert)

We are seeking a design of our menu. We would like something fresh looking in line with popular upper scale gastro pub/restaurant chains.

Clean looking, wish to keep colour palate similar to our logo or complimentary scheme. Like the black background but am open to other options.

We have listed our current menus for you to use their contents only. We do not wish to have anything similar to the current menu design.

Our website is www.mcfarrellstavern.com

Industry/Entity Type

Restaurant

Requirements
Must have
• Must have a menu for
• 11x 17" Dinner double sided
• 11x17" Lunch one side, Brunch other side Different colours than Dinner with Brunch leaning towards a brighter pallet
• 4.25 x 11 Beverage (Bar)
• 8.5x11 trifold Takeaway menu

```html
<!DOCTYPE html>
<html lang="en">
<head>
<meta charset="utf-8">
<title>McFarrell's Dinner Menu</title>
<link href="https://fonts.googleapis.com/css2?family=Oswald:wght@300;400;500&family=Permanent+Marker&display=swap" rel="stylesheet">
<style>
:root{
  --page:#ffffff;
  --board:#2c2c2c;
  --frame:#e8e8e8;
  --ink:#f1f1f1;
  --accent:#c59a6a;
}
*{margin:0;padding:0;box-sizing:border-box}
html,body{width:1200px;height:926px;overflow:hidden;background:var(--page)}
body{position:relative;font-family:"Oswald",sans-serif;color:var(--ink)}
.menu-side{position:absolute;background:var(--board);overflow:hidden}
.menu-side::after{content:"";position:absolute;inset:7px;border:2px solid var(--frame);pointer-events:none}
.side-front{left:52px;top:169px;width:524px;height:604px}
.side-back{left:635px;top:167px;width:517px;height:603px}

.menu-title{position:absolute;left:0;right:0;top:30px;height:60px;display:flex;justify-content:center;align-items:center;gap:6px;white-space:nowrap;font-family:"Permanent Marker",cursive;font-weight:400;font-size:50px;line-height:1;letter-spacing:1px}
.menu-title .star{width:20px;height:20px;margin-top:26px;flex:none}
.menu-title .star svg{display:block;width:20px;height:20px;fill:var(--accent)}
.title-rule{position:absolute;left:50%;transform:translateX(-50%);top:94px;width:120px;border-top:2px solid var(--ink)}

.column{position:absolute;top:0;bottom:0}
.section-heading{position:absolute;white-space:nowrap;font-family:"Permanent Marker",cursive;font-weight:400;font-size:26px;line-height:1;padding-bottom:3px;border-bottom:3px double var(--ink)}
.align-left .section-heading{left:0}
.align-right .section-heading{right:0}
.dish{position:absolute;left:0;right:0}
.dish-name{font-weight:400;font-size:10px;line-height:13px;color:var(--accent);letter-spacing:.5px;text-transform:uppercase;white-space:nowrap}
.align-right .dish-name{text-align:right}
.dish-text{margin-top:3px;font-weight:300;font-size:6.8px;line-height:10px;text-transform:uppercase;text-align:left}
.dish-text.bold{font-weight:500}

.brand-name{position:absolute;left:0;right:0;text-align:center;font-family:"Oswald",sans-serif;font-weight:400;font-size:19px;line-height:1;letter-spacing:1px;color:var(--ink)}
.side-front .brand-name{top:578px}
.side-back .brand-name{top:568px}

.sides-list{position:absolute;left:20px;right:0;top:508px;display:flex;justify-content:space-between;font-weight:300;font-size:6.8px;line-height:10px;text-transform:uppercase}
.sides-list span:nth-child(2){padding-top:5px}
.sides-list span:last-child{text-align:right}
</style>
</head>
<body>

<section class="menu-side side-front">
  <h1 class="menu-title"><span class="star"><svg viewBox="0 0 20 20"><polygon points="10,1 12.6,7.4 19.5,7.6 14,11.8 16,18.5 10,14.5 4,18.5 6,11.8 0.5,7.6 7.4,7.4"/></svg></span>DINNER<span class="star"><svg viewBox="0 0 20 20"><polygon points="10,1 12.6,7.4 19.5,7.6 14,11.8 16,18.5 10,14.5 4,18.5 6,11.8 0.5,7.6 7.4,7.4"/></svg></span></h1>
  <div class="title-rule"></div>

  <div class="column align-left" style="left:26px;width:212px">
    <h2 class="section-heading" style="top:136px">SALADS &amp; SOUPS</h2>
    <div class="dish" style="top:182px"><div class="dish-name">Arden Fresh Salad</div><p class="dish-text">We've sourced the best greens and the freshest vegetables around and we're bringing them from the farms to your plate! Top with our homemade sweet tomato vinaigrette and your taste buds will be doing a wee jig. 9</p></div>
    <div class="dish" style="top:263px"><div class="dish-name">Seafood Chowder</div><p class="dish-text">Chock full of the freshest seafood. Our rich, thick and creamy chowder is brimming with scallops, lobster, shrimp, haddock and salmon, thickened with a buttery potato slurry. Cup 8 | Bowl 14</p></div>
    <div class="dish" style="top:343px"><div class="dish-name">Caesar Salad</div><p class="dish-text">They say "don't mess with perfection." We say "just watch us!" We're elevating this classic with crisp romaine, maple candied bacon, Irish cheese and house made soda bread croutons all dressed with rich caesar dressing. 10 Add chicken 4</p></div>
    <div class="dish" style="top:414px"><div class="dish-name">Yesterday's Soup</div><p class="dish-text">Everyone knows soup is better the next day! This soup was made yesterday with the freshest ingredients. We've let the flavors meld overnight and today its perfection! Cup 5 | Bowl 8</p></div>
    <div class="dish" style="top:495px"><div class="dish-name">Fresh Beet Salad</div><p class="dish-text">The beet goes on! With our freshly prepared beets served with a bed of peppery arugula and fresh spinach, topped with creamy goat cheese, candied walnuts and a rich, deep maple balsamic dressing.</p></div>
  </div>

  <div class="column align-right" style="left:270px;width:229px">
    <h2 class="section-heading" style="top:137px">STARTERS</h2>
    <div class="dish" style="top:182px"><div class="dish-name">Scotch Egg</div><p class="dish-text bold">There's nothing better than a scotch egg! A perfectly boiled egg encased in savory sausage meat, fried until golden and served open face. Drizzled with a sweet honey and grainy mustard sauce. 9</p></div>
    <div class="dish" style="top:239px"><div class="dish-name">Classic Mussels</div><p class="dish-text">We take a generous 1 ½ pound stack of fresh mussels, steam them in a buttery white wine broth add a hint of garlic and herbs then finish with green onion. Absolutely awesome! Served with grilled artisan potato bread. 12</p></div>
    <div class="dish" style="top:298px"><div class="dish-name">Smoked Chicken Wings</div><p class="dish-text">These succulent wings are smoked in-house (need we say more?) and served with a house made tangy-sweet sticky glaze. We've taken this old standard and elevated it to a new favorite! 15</p></div>
    <div class="dish" style="top:352px"><div class="dish-name">Pub Style Nachos</div><p class="dish-text">Heaps of fresh corn chips topped with a generous helping of tomatoes, green pepper, red onions, black olives, jalapeno peppers, and warm, house blend of melted cheese. Served with a fresh homemade salsa and sour cream. 14 Add chicken 4</p></div>
    <div class="dish" style="top:419px"><div class="dish-name">Drunken Irish Mussels</div><p class="dish-text">We take mussels to a whole new level! 1 ½ pounds of fresh mussels steamed in Dunmore Stout, then stepped up with some double smoked bacon and fresh green onion. Finished with herbs and served with grilled artisan potato bread. These mussels are divine and drunk! 14</p></div>
    <div class="dish" style="top:485px"><div class="dish-name">McFarrell's Seafood &amp; Spinach Dip</div><p class="dish-text">This rich and satisfyingly gooey dip is the perfect blend of seafood and cheese! Served warm with corn chips and fried naan bread. This is a favorite dish. Go ahead and indulge! 15</p></div>
  </div>

  <div class="brand-name">McFarrell's</div>
</section>

<section class="menu-side side-back">
  <h1 class="menu-title"><span class="star"><svg viewBox="0 0 20 20"><polygon points="10,1 12.6,7.4 19.5,7.6 14,11.8 16,18.5 10,14.5 4,18.5 6,11.8 0.5,7.6 7.4,7.4"/></svg></span>DINNER<span class="star"><svg viewBox="0 0 20 20"><polygon points="10,1 12.6,7.4 19.5,7.6 14,11.8 16,18.5 10,14.5 4,18.5 6,11.8 0.5,7.6 7.4,7.4"/></svg></span></h1>
  <div class="title-rule"></div>

  <div class="column align-left" style="left:20px;width:236px">
    <h2 class="section-heading" style="top:112px">MAINS</h2>
    <div class="dish" style="top:160px"><div class="dish-name">Centenial Beer Battered Fish and Chips</div><p class="dish-text">We've paired two local legends: Irish lager and a fresh fillet. We've lightly battered it and we're serving it up with thick cut fries, our own "chiside" slaw and a serving of homemade tartar sauce. 16</p></div>
    <div class="dish" style="top:226px"><div class="dish-name">Trinity Bay Fish Cakes</div><p class="dish-text">Our cakes are made the traditional way: with salt cod. Staying with tradition, we're serving them up pan fried not deep fried. Served with side salad and homemade chow chow. 12</p></div>
    <div class="dish" style="top:286px"><div class="dish-name">Matilda's Pan Seared Haddock</div><p class="dish-text">Our generous haddock fillet is lightly floured and pan seared to golden brown. Served with buttery mash and seasonal veg with a side of our homemade tartar sauce. 14</p></div>
    <div class="dish" style="top:338px;right:-30px"><div class="dish-name">Planked Salmon with Maple Mustard &amp; Whiskey Sauce</div><p class="dish-text" style="margin-right:30px">A flakey fillet of salmon, slow roasted on a cedar plank then topped with a delectable maple mustard and whiskey sauce. Served with our buttery mash and fresh seasonal veg. 20</p></div>
    <div class="dish" style="top:392px"><div class="dish-name">Traditional Corned Beef and Cabbage</div><p class="dish-text">Having memories of comfort food and a home cooked dinner? Look no further than this rich and tasty and savory combination. Just like grandma made. 14</p></div>
    <div class="dish" style="top:447px"><div class="dish-name">Chicken Hot Pie</div><p class="dish-text bold">Comfort food at its finest! Our creamy pot pie has tender chunks of chicken, carrots, and peas all smothered in a rich, tasty sauce, topped with a buttery biscuit crust. Served with a farmer's salad. 14</p></div>
    <div class="dish" style="top:511px"><div class="dish-name">Ribeye Steak</div><p class="dish-text bold">We take a peak of tenderness, aged and trimmed 12oz AAA ribeye, high-temp charbroil it to your exact specifications and let the steak do the talking. Served with grilled vegetables, your choice of side and grilled artisan potato bread. 25</p></div>
  </div>

  <div class="column align-right" style="left:264px;width:235px">
    <div class="dish" style="top:121px"><div class="dish-name" style="text-align:left">Tikka Curry</div><p class="dish-text bold">Take an awesome blend of pulled chicken and fresh garden vegetables and slow cook them in a flavor filled house made curry sauce. This dish is pleasantly aromatic and not overly spicy (we can amp it up if you like). Served with naan and over a bed of basmati rice. 15</p></div>
    <div class="dish" style="top:186px"><div class="dish-name">Bangers ans Smash</div><p class="dish-text">Bangers and mash: two juicy sausages served on top of our homemade buttery champ, sauerkraut then smothered in a mouth-watering maple whiskey sauce. 14</p></div>
    <div class="dish" style="top:230px"><div class="dish-name">Dubliner Chicken</div><p class="dish-text">A local favorite! Fresh, tender chicken breast chock-full with a savory apple and onion stuffing smothered in a white wine sauce. Served with buttery champ and seasonal vegetable medley. 17</p></div>
    <div class="dish" style="top:285px"><div class="dish-name">Irish Sheperds Pie</div><p class="dish-text">A flavorful combination of braised beef and pork simmered in a demi-glace with traditional veg then topped with champ and slow baked to golden brown perfection. Served with a farmer's salad. 15</p></div>
    <div class="dish" style="top:341px"><div class="dish-name">McFarrell's Burger</div><p class="dish-text">This is one bangin' burger! One half-pound all beef patty topped with double smoked bacon, spinach, red onion, tomato, Dunmore Stout cheese, our special Lady Harrow relish and a fried egg on a potato-bread bun. Served with thick cut fries and our "chi-side" slaw. 15</p></div>
    <div class="dish" style="top:410px"><div class="dish-name">Bacon Cheddar Burger</div><p class="dish-text">A massive juicy half-pound all beef patty topped with three-blend cheese and smoked bacon. It's straight forward and to the point awesomeness on a potato-bread bun. 14</p></div>
    <h2 class="section-heading" style="top:467px">SIDES</h2>
    <div class="sides-list">
      <span>Garden Salad 4<br>Chi-Side Slaw 3</span>
      <span>Side of Thick Cut Fries 5<br>Baked Beans 4</span>
      <span>Champ 4<br>Stout Gravy 3</span>
    </div>
  </div>

  <div class="brand-name">McFarrell's</div>
</section>

</body>
</html>
```